Design home page for quorvant.xyz

We’re seeking a sleek, lead-generation-focused single-page website for Quorvant.xyz that communicates our expertise in delivering high-intent leads to mid-sized businesses. The goal is to guide visitors toward scheduling a free consultation while emphasizing our performance-based approach and comprehensive service offerings.

Industry/Entity Type

Marketing

Number of Pages Required

1 page

Font styles to use
Sans Serif

Requirements
Must have
• content from https://pages.tillowmark.com/doc/d/7hRtWqLMPZX402KDNe19sbYQ3Vb8FkwTtPa6Ue2kHLSF/view?tab=t.0
Nice to have
• color pallet from here https://pages.tillowmark.com/doc/d/9kwebRA4-ZQTofCVyLpHmn52bPWJ83gdX5fjroarr7T/view?tab=t.0

```html
<!DOCTYPE html>
<html lang="en">
<head>
<meta charset="utf-8">
<title>Quorvant.xyz — High-Intent Leads</title>
<link href="https://fonts.googleapis.com/css2?family=Montserrat:wght@600;700;800;900&family=Raleway:wght@200;300;400;500&family=Barlow+Semi+Condensed:wght@600&display=swap" rel="stylesheet">
<style>
  :root{
    --navy:#141d33;
    --navy-deep:#0f1628;
    --cream:#f2ece2;
    --ink:#f1ece3;
    --gold:#e9d197;
    --red:#c0261c;
    --red-dark:#8f1a12;
    --muted:#8d8882;
    --label:#4a4743;
  }
  *{box-sizing:border-box;margin:0;padding:0}
  html,body{width:1200px;height:851px;overflow:hidden;background:var(--navy-deep)}
  .page{position:relative;width:1200px;height:851px;overflow:hidden;background:var(--navy)}
  .hero-art{
    position:absolute;inset:0 0 120px 0;
    background:
      radial-gradient(ellipse 300px 70px at 600px 300px, rgba(233,209,151,.35), transparent 70%),
      radial-gradient(ellipse 280px 45px at 600px 345px, rgba(192,38,28,.35), transparent 70%),
      radial-gradient(ellipse 300px 50px at 600px 395px, rgba(43,111,128,.45), transparent 70%),
      radial-gradient(circle at 600px 420px, rgba(60,90,110,.35) 0, rgba(40,60,80,.2) 260px, transparent 520px),
      radial-gradient(circle at 110px 480px, rgba(180,120,80,.12), transparent 260px),
      radial-gradient(circle at 1090px 400px, rgba(180,120,80,.14), transparent 280px),
      linear-gradient(180deg, #16203a 0%, #18243d 55%, #121a2e 100%);
  }
  .brand{
    position:absolute;left:34px;top:30px;
    display:flex;align-items:center;gap:10px;
    font-family:"Raleway",sans-serif;font-weight:500;font-size:24px;
    color:var(--gold);letter-spacing:.06em;text-transform:uppercase;
  }
  .brand .mark{width:12px;height:12px;background:var(--gold)}
  .headline{position:absolute;left:0;right:0;top:150px;text-align:center}
  .headline .kicker{
    font-family:"Barlow Semi Condensed",sans-serif;font-weight:600;
    font-size:40px;line-height:1;color:var(--gold);letter-spacing:.01em;
  }
  .headline .main{
    font-family:"Montserrat",sans-serif;font-weight:900;
    font-size:108px;line-height:.9;color:var(--ink);letter-spacing:-.06em;
    margin-top:8px;
  }
  .headline .sub{
    font-family:"Raleway",sans-serif;font-weight:200;
    font-size:40px;line-height:1.12;color:var(--ink);margin-top:18px;letter-spacing:-.01em;
  }
  .intro{
    position:absolute;left:0;right:0;top:438px;text-align:center;
    font-family:"Raleway",sans-serif;font-weight:300;font-size:15px;line-height:24px;color:#fff;
  }
  .invite{
    position:absolute;left:0;right:0;top:547px;text-align:center;
    font-family:"Raleway",sans-serif;font-weight:400;font-size:15px;line-height:24px;color:var(--gold);
  }
  .footer-band{position:absolute;left:0;right:0;bottom:0;height:200px}
  .footer-band svg{position:absolute;inset:0}
  .cta{
    position:absolute;left:410px;top:628px;width:381px;height:64px;
    display:flex;align-items:center;justify-content:center;
    background:linear-gradient(180deg,#d63a2c 0%,var(--red) 45%,var(--red-dark) 100%);
    border:1px solid #e2554a;border-radius:4px;
    box-shadow:0 10px 22px rgba(0,0,0,.25);
    font-family:"Montserrat",sans-serif;font-weight:800;font-size:20px;color:#fff;
    text-shadow:0 1px 2px rgba(0,0,0,.35);text-decoration:none;letter-spacing:.01em;
  }
  .featured{position:absolute;left:0;right:0;top:772px;height:40px;display:flex;align-items:center}
  .featured .label{
    position:absolute;left:156px;
    font-family:"Montserrat",sans-serif;font-weight:600;font-size:8px;letter-spacing:.12em;color:var(--label);
  }
  .outlet{
    position:absolute;transform:translateX(-50%);white-space:nowrap;
    font-family:"Montserrat",sans-serif;font-weight:700;font-size:15px;color:var(--muted);
  }
</style>
</head>
<body>
<main class="page">
  <div class="hero-art" role="img" aria-label="Abstract data visualisation of radiating lines, numbered nodes and gold, red and teal light wisps converging at the centre"></div>

  <div class="brand"><span class="mark"></span>quorvant.xyz</div>

  <h1 class="headline">
    <div class="kicker">HIGH-INTENT</div>
    <div class="main">LEADS</div>
    <div class="sub">DELIVERED DIRECTLY<br>TO YOUR PIPELINE</div>
  </h1>

  <p class="intro">Take the guesswork out of lead generation. We connect you with<br>high-intent prospects who are genuinely interested in what you offer,<br>helping you grow your sales pipeline with ease.</p>

  <p class="invite">LET’S TALK ABOUT HOW WE CAN DELIVER<br>THE LEADS YOUR BUSINESS NEEDS.</p>

  <div class="footer-band">
    <svg width="1200" height="200" viewBox="0 0 1200 200" aria-hidden="true">
      <path d="M0 8 Q600 34 1200 8 L1200 200 L0 200 Z" fill="var(--cream)"/>
    </svg>
  </div>

  <a class="cta" href="#">SCHEDULE A FREE CALL TODAY</a>

  <div class="featured">
    <span class="label">Featured on :</span>
    <span class="outlet" style="left:314px">Ledger Wire</span>
    <span class="outlet" style="left:474px">Brandloom</span>
    <span class="outlet" style="left:634px">AdCrest</span>
    <span class="outlet" style="left:809px">Northfield Media</span>
    <span class="outlet" style="left:988px">Signal Trade News</span>
  </div>
</main>
</body>
</html>
```